Website Design for Solar Panel Company

We are working with a company called LumaRX.

Some sites to use for content/competitors and inspiration:
https://www.brightvela.com
https://prod.cdn-prod.heliqor.com
https://corvaltpower.net
https://www.mirodyne.com/solarpanels

Thank you for taking the time to consider designing a website for us. We are web developers based in Stockton, CA, USA. Most of our projects go through the same process. Understanding this process may help you win a project with us. We custom-code all of our websites in-house. We don’t have any requirements as to what tools you use for your design, but we prefer Figma files. For any design that we label as four-stars, we send it to the client for review. The client picks the final design they want us to use. Once we complete this process, we will continue to show additional clients all the four-star sites and purchase them later. Your designs will have multiple chances to sell. For better chances of success, we ask that you follow these guidelines.

IMAGES:
If you use any images or icons in the design, we ask that you have a link to the asset so we can purchase the image/icon. Most of the designs we submit do not have the customer’s images on them unless they have some great images. Be creative; show us the feeling you are trying to portray with your image choices. Use any royalty-free site you choose. We subscribe to Adobe and mainly use their images, but we can purchase images outside of Adobe. PLEASE NOTE: we will not submit designs to clients with watermarks on the images.

FONTS:
We ask that you identify the fonts used in the design. This can be done in a message if you want. We typically use Google Fonts and Adobe Fonts.

CONTENT:
We're always open to different content and ideas. We often submit designs with stock images so the client can see our vision. We typically take pictures after the website launch to use their images with our vision. Lorem Ipsum is fine for paragraphs, but we ask that you write the headers in correct English. We want to be able to show the vision and identify the sections of the website.

INSPIRATION:
We typically add a couple of links in the brief of websites we like to help you get started in your design.

REVISIONS:
We do not often ask for revisions of the designs unless we see something in the design that may not appeal to the client. If there are slight changes that we want to make, we do that in the development process.

FEEDBACK:
We rarely give feedback on designs during the design process. We are working on many website projects and do not have the time to provide feedback. We usually respond if your request is well thought out and asks specific questions, but a note asking “feedback, please” usually goes unanswered.

```html
<!DOCTYPE html>
<html lang="en">
<head>
<meta charset="utf-8">
<title>LumaRX — Solar Energy</title>
<link href="https://fonts.googleapis.com/css2?family=Open+Sans:wght@400;500;600;700;800&display=swap" rel="stylesheet">
<style>
:root{
  --navy:#17406d;
  --navy-deep:#10294b;
  --topbar:#1f2235;
  --green:#6dbf2b;
  --ink:#1c1c1c;
  --muted:#7a7f88;
  --light:#f4f4f5;
  --white:#ffffff;
  --line:#d9dce1;
}
*{margin:0;padding:0;box-sizing:border-box}
html,body{width:1200px;height:4841px;overflow:hidden}
body{font-family:"Open Sans",Arial,sans-serif;color:var(--ink);background:var(--white);position:relative}
.abs{position:absolute}
a{color:inherit;text-decoration:none}
.btn{position:absolute;display:flex;align-items:center;justify-content:center;gap:12px;background:var(--green);color:#fff;font-weight:700;font-size:15px;border-radius:2px}
.eyebrow{position:absolute;font-size:12px;color:var(--green);text-decoration:underline;text-underline-offset:3px;letter-spacing:.2px}
.h2{position:absolute;color:var(--navy);font-weight:700;font-size:40px;line-height:1.25}
.para{position:absolute;color:var(--muted);font-size:13px;line-height:22px}

.topbar{top:0;left:0;width:1200px;height:47px;background:var(--topbar);color:#c9cbd4;font-size:14px}
.topbar span{position:absolute;top:14px}
.social-dot{position:absolute;top:17px;width:12px;height:12px;border-radius:2px;background:#9ea2b2}

.header{top:47px;left:0;width:1200px;height:111px;background:#fff}
.brand{position:absolute;font-weight:800;font-size:38px;letter-spacing:.5px;color:var(--ink)}
.brand-sq{position:absolute;width:14px;height:14px;background:var(--green)}
.contact-item{position:absolute;font-size:15px;color:var(--ink)}
.contact-item small{display:block;font-size:13px;color:var(--muted);margin-top:4px}
.estimate{position:absolute;left:957px;top:29px;width:181px;height:50px;background:var(--navy);color:#fff;border-radius:4px;font-weight:700;font-size:14px;display:flex;align-items:center;justify-content:center;gap:10px}

.hero{top:158px;left:0;width:1200px;height:790px;background:linear-gradient(160deg,#3f6b88 0%,#56758a 30%,#2c4a63 60%,#1e3550 100%)}
.nav{position:absolute;left:79px;top:0;width:984px;height:64px;background:#fff;z-index:2}
.nav a{font-size:14px;color:#6b6f78;position:absolute;top:22px}
.nav a.active{color:var(--navy);font-weight:600}
.nav-phone{position:absolute;left:1063px;top:0;width:75px;height:64px;background:var(--navy-deep);z-index:2;display:flex;align-items:center;justify-content:center}
.tag{position:absolute;left:100px;top:293px;width:268px;height:41px;background:var(--navy);border-left:4px solid var(--green);color:#fff;font-weight:700;font-size:20px;padding:6px 18px}
.hero h1{position:absolute;left:98px;top:360px;color:#fff;font-size:60px;font-weight:700;letter-spacing:.5px}
.hero p{position:absolute;left:101px;top:453px;width:470px;color:#f1f3f5;font-size:17px;line-height:27px}

.photo{position:absolute}
.power-btn{position:absolute;left:818px;top:1231px;width:80px;height:80px;border-radius:50%;background:var(--navy);display:flex;align-items:center;justify-content:center}

.services{top:1559px;left:0;width:1200px;height:648px;background:var(--light)}
.svc{position:absolute;top:208px;width:318px;height:353px;border-radius:4px;overflow:hidden}
.svc h3{position:absolute;left:28px;top:230px;color:#fff;font-size:23px;font-weight:700}
.svc .dot{position:absolute;left:24px;top:232px;width:14px;height:14px;border-radius:50%;background:var(--green)}
.svc .go{position:absolute;left:26px;top:278px;width:50px;height:50px;border-radius:50%;background:rgba(255,255,255,.18);display:flex;align-items:center;justify-content:center}

.experts{top:2207px;left:0;width:1200px;height:385px;background:linear-gradient(100deg,#20324a 0%,#2c3b52 45%,#6a5156 75%,#a2674f 100%)}
.exp-card{position:absolute;top:2319px;width:231px;height:361px;background:#fff;box-shadow:0 6px 18px rgba(0,0,0,.08);text-align:center}
.exp-card h4{margin-top:100px;color:var(--navy);font-size:19px;font-weight:700}
.exp-card p{margin:16px auto 0;width:170px;font-size:14px;line-height:25px;color:var(--navy)}
.exp-card .more{display:block;margin-top:28px;font-size:14px;font-weight:700;color:var(--navy-deep)}
.exp-card svg.ic{position:absolute;left:50%;top:44px;transform:translateX(-50%)}

.slide{position:absolute;top:2879px;height:379px}
.arrow-c{position:absolute;width:38px;height:38px;border-radius:50%;background:#fff;display:flex;align-items:center;justify-content:center}

.testi{top:3335px;left:0;width:1200px;height:530px;background:var(--navy-deep)}
.t-card{position:absolute;top:211px;width:321px;height:216px;background:#1f3b62;border-radius:4px}
.t-card .q{position:absolute;left:142px;top:-6px;color:var(--green);font-size:64px;font-weight:800;line-height:1;font-family:Georgia,serif}
.t-card p{position:absolute;left:32px;top:38px;width:266px;color:#fff;font-size:13px;line-height:23px}
.t-card .av{position:absolute;left:28px;top:144px;width:48px;height:48px;border-radius:50%;background:linear-gradient(135deg,#c9b39a,#7c6a5a);border:2px solid #fff}
.t-card .nm{position:absolute;left:92px;top:149px;color:#fff;font-weight:600;font-size:16px}
.t-card .ct{position:absolute;left:92px;top:172px;color:#8e9bb0;font-size:15px}

.c-item{position:absolute;left:188px;font-size:12px;font-weight:700;color:var(--ink)}
.c-item small{display:block;font-weight:400;font-size:13px;color:var(--muted);margin-top:3px}
.c-ic{position:absolute;left:112px;width:42px;height:42px;border-radius:50%;background:#eef6e7;display:flex;align-items:center;justify-content:center}
.form{top:3978px;left:601px;width:494px;height:567px;background:#fff;border-top:5px solid var(--navy);box-shadow:0 8px 30px rgba(0,0,0,.08);z-index:2}
.form h3{position:absolute;left:38px;top:50px;font-size:25px;font-weight:700;color:var(--ink)}
.form label{position:absolute;font-size:13px;font-weight:600;color:var(--ink)}
.field{position:absolute;height:43px;border:1px solid #c7cbd1;border-radius:22px;font-size:13px;color:#9a9ea6;padding:12px 24px}

.f-info{position:absolute;top:4615px;color:#fff;font-size:13px;line-height:19px}
.f-nav{position:absolute;left:256px;top:4681px;width:688px;height:86px;border-top:1px solid #36507a;border-bottom:1px solid #36507a}
.f-nav a{position:absolute;top:33px;color:#fff;font-size:14px}
.f-soc{position:absolute;top:4792px;width:26px;height:26px;border:1px solid #fff}
.f-soc i{position:absolute;left:8px;top:8px;width:8px;height:8px;background:#fff;border-radius:1px}
</style>
</head>
<body>

<div class="abs topbar">
  <svg class="abs" style="left:78px;top:17px" width="14" height="14" viewBox="0 0 14 14"><circle cx="7" cy="7" r="6" fill="none" stroke="#6dbf2b" stroke-width="1.5"/><path d="M7 3.5V7l2.3 1.5" stroke="#6dbf2b" stroke-width="1.5" fill="none"/></svg>
  <span style="left:102px">Mon-Sat: 09am to 07:30pm</span>
  <svg class="abs" style="left:324px;top:18px" width="15" height="11" viewBox="0 0 15 11"><rect x=".75" y=".75" width="13.5" height="9.5" fill="none" stroke="#6dbf2b" stroke-width="1.5"/><path d="M1 1l6.5 5L14 1" fill="none" stroke="#6dbf2b" stroke-width="1.5"/></svg>
  <span style="left:348px">hello@lumarx.com</span>
  <span style="left:877px;top:10px;height:26px;border-left:1px solid #444a5e"></span>
  <span style="left:887px">Faqs</span>
  <span style="left:938px;top:10px;height:26px;border-left:1px solid #444a5e"></span>
  <span style="left:953px">Pricing</span>
  <span style="left:1017px;top:10px;height:26px;border-left:1px solid #444a5e"></span>
  <i class="social-dot" style="left:1036px"></i>
  <i class="social-dot" style="left:1062px"></i>
  <i class="social-dot" style="left:1090px"></i>
  <i class="social-dot" style="left:1123px"></i>
</div>

<header class="abs header">
  <div class="brand-sq" style="left:102px;top:43px"></div>
  <div class="brand" style="left:124px;top:27px">LumaRX</div>
  <svg class="abs" style="left:362px;top:37px" width="36" height="36" viewBox="0 0 36 36"><path d="M6 10c0-3 4-5 12-5s12 2 12 5l-2 4h-5l-1-3h-8l-1 3H8z" fill="none" stroke="#17406d" stroke-width="2"/><rect x="10" y="17" width="16" height="12" rx="2" fill="none" stroke="#17406d" stroke-width="2"/><circle cx="18" cy="23" r="3" fill="none" stroke="#17406d" stroke-width="2"/></svg>
  <div class="contact-item" style="left:413px;top:30px">+1-209-555-0147<small>Need help? Make a Call</small></div>
  <svg class="abs" style="left:664px;top:35px" width="34" height="34" viewBox="0 0 34 34"><circle cx="17" cy="17" r="14" fill="none" stroke="#17406d" stroke-width="2"/><ellipse cx="17" cy="17" rx="6" ry="14" fill="none" stroke="#17406d" stroke-width="2"/><path d="M3 17h28M5 10h24M5 24h24" stroke="#17406d" stroke-width="2"/></svg>
  <div class="contact-item" style="left:712px;top:30px">USA<small>48 Harbor Lane, Stockton</small></div>
  <div class="estimate">Free Estimate
    <svg width="20" height="20" viewBox="0 0 20 20"><circle cx="10" cy="10" r="8.5" fill="none" stroke="#fff" stroke-width="1.5"/><path d="M6 10h8M11 7l3 3-3 3" fill="none" stroke="#fff" stroke-width="1.5"/></svg>
  </div>
</header>

<section class="abs hero" role="img" aria-label="Photo of a technician in a hard hat installing rooftop solar panels">
  <nav class="nav">
    <a class="active" style="left:86px">Home</a>
    <a style="left:198px">About Us</a>
    <a style="left:310px">Services</a>
    <a style="left:423px">Gallery</a>
    <a style="left:541px">Our Team</a>
    <a style="left:692px">Contact Us</a>
  </nav>
  <div class="nav-phone">
    <svg width="40" height="40" viewBox="0 0 24 24"><path d="M5 3h4l2 5-2.5 1.5a11 11 0 005 5L15 12l5 2v4a2 2 0 01-2 2A16 16 0 013 5a2 2 0 012-2z" fill="none" stroke="#fff" stroke-width="1.3"/></svg>
  </div>
  <div class="tag">Unleash</div>
  <h1>A sustainable tomorrow</h1>
  <p>Lorem ipsum dolor sit amet, consectetur adipiscing elit, sed do eiusmod tempor i</p>
  <a class="btn" style="left:100px;top:531px;width:176px;height:51px">Read More</a>
</section>
<svg class="abs" style="left:0;top:800px" width="1200" height="160" viewBox="0 800 1200 160">
  <path d="M0 935 Q650 905 1200 822 L1200 960 L0 960Z" fill="#fff"/>
  <path d="M0 918 Q360 912 690 892 Q360 928 0 952Z" fill="#6dbf2b"/>
</svg>

<section>
  <div class="eyebrow" style="left:94px;top:1061px">WHO WE ARE</div>
  <h2 class="h2" style="left:94px;top:1096px">Brighten your day,<br>Power with solar</h2>
  <div class="abs" style="left:94px;top:1222px;font-size:20px;font-weight:600;color:var(--ink)">Harnessing solar energy for a cleaner tomorrow</div>
  <p class="para" style="left:94px;top:1269px;width:506px">Lorem ipsum dolor sit amet, consectetur adipiscing elit, sed do eiusmod temp or incididunt ut labore et dolore magna aliqua. Ut enim ad minim veniam, quis laboris nisi ut aliquip ex ea commodo consequat.</p>
  <p class="para" style="left:94px;top:1346px;width:506px">Lorem ipsum dolor sit amet, consectetur adipiscing elit, sed do eiusmod temp or incididunt ut labore et dolore magna aliqua.</p>
  <a class="btn" style="left:92px;top:1427px;width:155px;height:45px">Contact us
    <svg width="18" height="12" viewBox="0 0 18 12"><path d="M0 6h16M11 1l5 5-5 5" fill="none" stroke="#fff" stroke-width="1.6"/></svg></a>
  <div class="photo" role="img" aria-label="Photo of two installers placing solar panels on a rooftop" style="left:618px;top:1044px;width:234px;height:423px;background:linear-gradient(170deg,#c9b9a0 0%,#a58e74 35%,#6f7d8e 70%,#48576b 100%)"></div>
  <div class="photo" role="img" aria-label="Close-up photo of solar panels with trees behind" style="left:870px;top:1072px;width:234px;height:427px;background:linear-gradient(175deg,#8fae8c 0%,#b8c7cf 35%,#6e8aa6 65%,#3f4f62 100%)"></div>
  <div class="power-btn">
    <svg width="40" height="40" viewBox="0 0 40 40"><path d="M20 6v14" stroke="#fff" stroke-width="4" stroke-linecap="round"/><path d="M12 11a12 12 0 1016 0" fill="none" stroke="#fff" stroke-width="4" stroke-linecap="round"/></svg>
  </div>
</section>

<section class="abs services">
  <div class="eyebrow" style="left:90px;top:60px">OUR SERVICES</div>
  <h2 class="h2" style="left:86px;top:92px">Services We Provide</h2>
  <div class="abs" style="left:943px;top:110px;font-size:15px;color:var(--ink)">More Services</div>
  <div class="abs" style="left:1076px;top:99px;width:40px;height:38px;background:var(--green);display:flex;align-items:center;justify-content:center">
    <svg width="10" height="14" viewBox="0 0 10 14"><path d="M1 1l7 6-7 6z" fill="#fff"/></svg></div>
  <div class="svc" style="left:98px" role="img" aria-label="Photo of installers mounting panels on a tiled roof"><div style="position:absolute;inset:0;background:linear-gradient(180deg,#c9b59a 0%,#9c8670 40%,#3a342f 75%,#1c1a18 100%)"></div><i class="dot"></i><h3>Panel Installation</h3><div class="go"><svg width="16" height="14" viewBox="0 0 16 14"><path d="M1 7h13M9 2l5 5-5 5" fill="none" stroke="#fff" stroke-width="1.6"/></svg></div></div>
  <div class="svc" style="left:443px" role="img" aria-label="Photo of workers assessing a solar array"><div style="position:absolute;inset:0;background:linear-gradient(180deg,#b9c4cc 0%,#6e7f8f 40%,#2b3545 75%,#15191f 100%)"></div><i class="dot"></i><h3>Site Assessment</h3><div class="go"><svg width="16" height="14" viewBox="0 0 16 14"><path d="M1 7h13M9 2l5 5-5 5" fill="none" stroke="#fff" stroke-width="1.6"/></svg></div></div>
  <div class="svc" style="left:791px" role="img" aria-label="Photo of a technician carrying a panel across a field"><div style="position:absolute;inset:0;background:linear-gradient(180deg,#6f8f5e 0%,#a4b6b8 40%,#3b4a58 75%,#171b20 100%)"></div><i class="dot"></i><h3>Battery Backup</h3><div class="go"><svg width="16" height="14" viewBox="0 0 16 14"><path d="M1 7h13M9 2l5 5-5 5" fill="none" stroke="#fff" stroke-width="1.6"/></svg></div></div>
</section>

<section class="abs experts" role="img" aria-label="Photo of wind turbines and solar fields at sunset">
  <h2 class="abs" style="left:90px;top:110px;color:#fff;font-size:40px;font-weight:700;line-height:52px">Leading<br>Experts</h2>
  <a class="btn" style="left:92px;top:279px;width:155px;height:46px">Contact us
    <svg width="18" height="12" viewBox="0 0 18 12"><path d="M0 6h16M11 1l5 5-5 5" fill="none" stroke="#fff" stroke-width="1.6"/></svg></a>
</section>
<div class="exp-card" style="left:355px">
  <svg class="ic" width="42" height="42" viewBox="0 0 42 42"><circle cx="21" cy="21" r="6" fill="none" stroke="#17406d" stroke-width="2"/><path d="M21 4l3 5 6-1 1 6 5 3-3 5 3 5-5 3-1 6-6-1-3 5-3-5-6 1-1-6-5-3 3-5-3-5 5-3 1-6 6 1z" fill="none" stroke="#17406d" stroke-width="2" stroke-linejoin="round"/></svg>
  <h4>Expertise</h4><p>Lorem ipsum dolor sit consectetur adipiscing elit, sed do eiusmod tempor incididunt</p><span class="more">Read More &nbsp;→</span></div>
<div class="exp-card" style="left:614px">
  <svg class="ic" width="42" height="42" viewBox="0 0 42 42"><circle cx="19" cy="21" r="13" fill="none" stroke="#17406d" stroke-width="2"/><circle cx="28" cy="28" r="7" fill="#fff" stroke="#17406d" stroke-width="2"/><path d="M25 28l2 2 4-4" fill="none" stroke="#17406d" stroke-width="2"/></svg>
  <h4>Professional</h4><p>Lorem ipsum dolor sit consectetur adipiscing elit, sed do eiusmod tempor incididunt</p><span class="more">Read More &nbsp;→</span></div>
<div class="exp-card" style="left:875px">
  <svg class="ic" width="42" height="42" viewBox="0 0 42 42"><circle cx="21" cy="13" r="8" fill="none" stroke="#17406d" stroke-width="2"/><path d="M5 39c0-9 7-14 16-14s16 5 16 14z" fill="none" stroke="#17406d" stroke-width="2"/></svg>
  <h4>Experienced</h4><p>Lorem ipsum dolor sit consectetur adipiscing elit, sed do eiusmod tempor incididunt</p><span class="more">Read More &nbsp;→</span></div>

<section>
  <div class="eyebrow" style="left:0;width:1200px;text-align:center;top:2739px">OUR GALLERY</div>
  <h2 class="h2" style="left:0;width:1200px;text-align:center;top:2774px">Our Latest Projects</h2>
  <div class="slide" style="left:0;width:222px;background:linear-gradient(160deg,#c59c82 0%,#a5735a 40%,#3f5b86 70%,#2b3f62 100%)" role="img" aria-label="Photo of solar panels beside terracotta roof tiles"></div>
  <div class="slide" style="left:229px;width:740px;background:linear-gradient(160deg,#4f5a3c 0%,#6a6254 35%,#3a3d48 65%,#262a36 100%)" role="img" aria-label="Photo of workers installing panels on a tiled roof"></div>
  <div class="slide" style="left:977px;width:223px;background:radial-gradient(circle at 60% 30%,#ffe3a1 0%,#f29a4d 20%,#8a5467 45%,#2f4a8a 75%,#1c2f63 100%)" role="img" aria-label="Photo of a sun flare over a field of solar panels"></div>
  <div class="abs" style="left:229px;width:740px;top:3005px;text-align:center;color:#fff;font-size:36px;font-weight:700;line-height:49px">Latest Project in<br>California</div>
  <div class="abs" style="left:410px;width:380px;top:3120px;text-align:center;color:#fff;font-size:12px;line-height:19px">Lorem ipsum dolor sit amet, consectetur adipiscing elit, sed do eiusmod tempor incidid</div>
  <div class="arrow-c" style="left:253px;top:3048px"><svg width="14" height="12" viewBox="0 0 14 12"><path d="M13 6H2M6 1L1 6l5 5" fill="none" stroke="#222" stroke-width="1.6"/></svg></div>
  <div class="arrow-c" style="left:905px;top:3048px"><svg width="14" height="12" viewBox="0 0 14 12"><path d="M1 6h11M8 1l5 5-5 5" fill="none" stroke="#222" stroke-width="1.6"/></svg></div>
</section>

<section class="abs testi">
  <div class="eyebrow" style="left:0;width:1200px;text-align:center;top:54px">TESTIMONIALS</div>
  <h2 class="abs" style="left:0;width:1200px;text-align:center;top:90px;color:#fff;font-size:40px;font-weight:700">What Clients are Saying</h2>
  <div class="t-card" style="left:92px"><span class="q">”</span><p>Lorem ipsum dolor sit amet, consectetur adipiscing elit, sed do eiusmod tempor i ncididunt ut labore et dolore magna aliq ua. Ut enim ad minim veniam, quis nostr</p><i class="av"></i><span class="nm">Dara K.</span><span class="ct">Country</span></div>
  <div class="t-card" style="left:439px"><span class="q">”</span><p>Lorem ipsum dolor sit amet, consectetur adipiscing elit, sed do eiusmod tempor i ncididunt ut labore et dolore magna aliq ua. Ut enim ad minim veniam, quis nostr</p><i class="av"></i><span class="nm">Dara K.</span><span class="ct">Country</span></div>
  <div class="t-card" style="left:785px"><span class="q">”</span><p>Lorem ipsum dolor sit amet, consectetur adipiscing elit, sed do eiusmod tempor i ncididunt ut labore et dolore magna aliq ua. Ut enim ad minim veniam, quis nostr</p><i class="av"></i><span class="nm">Dara K.</span><span class="ct">Country</span></div>
  <svg class="abs" style="left:565px;top:452px" width="70" height="12" viewBox="0 0 70 12"><circle cx="4" cy="6" r="3" fill="#b8c2d2"/><circle cx="18" cy="6" r="3" fill="#b8c2d2"/><circle cx="34" cy="6" r="5" fill="none" stroke="#b8c2d2"/><circle cx="34" cy="6" r="2.5" fill="#b8c2d2"/><circle cx="50" cy="6" r="3" fill="#b8c2d2"/><circle cx="64" cy="6" r="3" fill="#b8c2d2"/></svg>
</section>

<svg class="abs" style="left:0;top:4300px" width="1200" height="541" viewBox="0 4300 1200 541">
  <path d="M0 4545 Q520 4420 1200 4398 L1200 4841 L0 4841Z" fill="#10294b"/>
  <path d="M1000 4382 Q1100 4350 1200 4336 L1200 4368 Q1100 4372 1000 4382Z" fill="#6dbf2b"/>
</svg>
<section>
  <h2 class="abs" style="left:107px;top:3975px;font-size:42px;color:var(--navy);font-weight:400"><b style="font-weight:700">Contact Us</b> Today</h2>
  <div class="c-ic" style="top:4046px"><svg width="26" height="26" viewBox="0 0 24 24"><path d="M5 3h4l2 5-2.5 1.5a11 11 0 005 5L15 12l5 2v4a2 2 0 01-2 2A16 16 0 013 5a2 2 0 012-2z" fill="none" stroke="#6dbf2b" stroke-width="1.4"/></svg></div>
  <div class="c-item" style="top:4054px">HEAD OFFICE<small>48 Harbor Lane, CA 95202</small></div>
  <div class="c-ic" style="top:4118px"><svg width="26" height="26" viewBox="0 0 26 26"><rect x="3" y="6" width="20" height="15" fill="none" stroke="#6dbf2b" stroke-width="1.4"/><path d="M3 6l10 8 10-8" fill="none" stroke="#6dbf2b" stroke-width="1.4"/></svg></div>
  <div class="c-item" style="top:4127px">EMAIL ADDRESS<small>team@lumarx.com</small></div>
  <div class="c-ic" style="top:4190px"></div>
  <div class="c-item" style="top:4193px">CALL US NOW<small>Call Now: 209-555-0147</small></div>
</section>
<div class="abs form">
  <h3>Send Us A Message</h3>
  <label style="left:38px;top:111px">First Name</label>
  <label style="left:252px;top:111px">Last Name</label>
  <div class="field" style="left:40px;top:133px;width:199px">John</div>
  <div class="field" style="left:252px;top:133px;width:199px">Doe</div>
  <label style="left:38px;top:197px">Email</label>
  <div class="field" style="left:40px;top:219px;width:417px">you@mailbox.com</div>
  <label style="left:38px;top:287px">Message</label>
  <div class="field" style="left:40px;top:309px;width:417px;height:125px;border-radius:2px">Type Your Message</div>
  <a class="btn" style="left:39px;top:473px;width:156px;height:45px">Contact us
    <svg width="18" height="12" viewBox="0 0 18 12"><path d="M0 6h16M11 1l5 5-5 5" fill="none" stroke="#fff" stroke-width="1.6"/></svg></a>
</div>

<footer>
  <div class="abs" style="left:128px;top:4614px;width:14px;height:14px;background:var(--green)"></div>
  <div class="abs" style="left:150px;top:4598px;color:#fff;font-weight:800;font-size:38px;letter-spacing:.5px">LumaRX</div>
  <div class="abs" style="left:410px;top:4610px;height:42px;border-left:1px solid #36507a"></div>
  <svg class="abs" style="left:430px;top:4618px" width="30" height="30" viewBox="0 0 30 30"><circle cx="15" cy="15" r="12" fill="none" stroke="#fff" stroke-width="1.6"/><ellipse cx="15" cy="15" rx="5" ry="12" fill="none" stroke="#fff" stroke-width="1.6"/><path d="M3 15h24" stroke="#fff" stroke-width="1.6"/></svg>
  <div class="f-info" style="left:470px">48 Harbor Lane, Suite 2<br>Stockton, CA 95202</div>
  <div class="abs" style="left:670px;top:4610px;height:42px;border-left:1px solid #36507a"></div>
  <svg class="abs" style="left:688px;top:4616px" width="28" height="32" viewBox="0 0 28 32"><rect x="4" y="2" width="14" height="28" rx="2" fill="none" stroke="#fff" stroke-width="1.6"/><path d="M21 11a6 6 0 010 10M24 8a10 10 0 010 16" fill="none" stroke="#fff" stroke-width="1.4"/></svg>
  <div class="f-info" style="left:725px">PHONE<br>(209) 555 0147</div>
  <div class="abs" style="left:846px;top:4610px;height:42px;border-left:1px solid #36507a"></div>
  <svg class="abs" style="left:864px;top:4620px" width="28" height="24" viewBox="0 0 28 24"><rect x="2" y="6" width="24" height="16" fill="none" stroke="#fff" stroke-width="1.6"/><path d="M2 6l12 9 12-9M8 2h12" fill="none" stroke="#fff" stroke-width="1.6"/></svg>
  <div class="f-info" style="left:904px">EMAIL<br>info@lumarx.com</div>
  <nav class="f-nav">
    <a style="left:19px">HOME</a><a style="left:113px">SERVICES</a><a style="left:220px">ABOUT US</a><a style="left:338px">TESTIMONIALS</a><a style="left:488px">BLOG</a><a style="left:581px">CONTACT US</a>
  </nav>
  <div class="abs" style="left:135px;top:4797px;color:#fff;font-size:12px">LumaRX</div>
  <div class="f-soc" style="left:933px"><i></i></div>
  <div class="f-soc" style="left:966px"><i></i></div>
  <div class="f-soc" style="left:999px"><i></i></div>
  <div class="f-soc" style="left:1032px"><i></i></div>
</footer>

</body>
</html>
```